Tri-fold flyer for Managed Services IT company

We need a tri-fold flyer design for our Managed Services IT company. Our website is here: https://pelicanfjordit.net. While we don't have to match our website we do want to incorporate the logo in the flyer. We would like a flyer that is *very* easy and quick to read/skim over and convey our message. Something like these:

https://www.artkestrel.com/design/58203917

https://47sketchyard.com/postcard-flyer-design/contests/create-lead-generating-flyer-postcard-managed-services-company-815243

http://www.marbleoaksystems.com/managed-services-no-cost-one-month/

Target Market(s)

Business to business IT services

Industry/Entity Type

It Service

Font styles to use
Serif
Sans Serif

Requirements
Must have
• *very* easy and quick to read/skim over and convey our message
Should not have
• verbose, lots of text

```html
<!DOCTYPE html>
<html lang="en">
<head>
<meta charset="utf-8">
<title>Pelican Fjord IT – Tri-fold Flyer</title>
<link rel="stylesheet" href="https://fonts.googleapis.com/css2?family=Montserrat:wght@400;600;800&family=Open+Sans:wght@400;600&display=swap">
<style>
  :root{
    --bg:#e9e9e9;
    --navy:#0d1f4d;
    --blue:#163a86;
    --royal:#1f56b8;
    --orange:#f28c1c;
    --white:#ffffff;
    --ink:#33405a;
    --muted:#c9d6f2;
    --photo-a:#5a6f96;
    --photo-b:#1b2a4e;
  }
  *{box-sizing:border-box;margin:0;padding:0}
  html,body{width:1200px;height:2400px;overflow:hidden;background:var(--bg)}
  body{position:relative;font-family:"Open Sans",Arial,sans-serif;color:var(--ink)}
  .panel{position:absolute;width:330px;height:720px;overflow:hidden}
  .spread{position:absolute;left:105px;width:990px;height:720px;box-shadow:0 6px 18px rgba(0,0,0,.18)}
  .spread .panel{top:0}
  .p1{left:0}.p2{left:330px}.p3{left:660px}
  .solo{left:435px;top:40px;box-shadow:0 6px 18px rgba(0,0,0,.18)}

  /* cover */
  .cover{background:var(--white)}
  .brand{display:flex;align-items:center;gap:8px;font-family:"Montserrat",sans-serif;font-weight:800;font-size:17px;color:var(--blue);letter-spacing:1px}
  .brand-dot{width:14px;height:14px;border-radius:50%;background:var(--orange)}
  .cover .brand{position:absolute;top:44px;left:0;right:0;justify-content:center}
  .cover-title{position:absolute;top:118px;left:24px;right:24px;text-align:center;font-family:"Montserrat",sans-serif;font-weight:800;font-size:19px;color:var(--blue);line-height:1.2}
  .cover-sub{position:absolute;top:176px;left:40px;right:40px;text-align:center;font-size:11px;color:var(--ink);line-height:1.4}
  .cover-photo{position:absolute;top:230px;left:0;width:330px;height:330px;background:radial-gradient(circle at 50% 40%,var(--photo-a),var(--photo-b))}
  .cover-band{position:absolute;top:560px;left:0;width:330px;height:160px;background:var(--navy)}
  .cover-band .cta{position:absolute;top:40px;left:24px;right:24px;background:var(--orange);color:var(--white);font-family:"Montserrat",sans-serif;font-weight:600;font-size:12px;text-align:center;padding:10px 6px;border-radius:3px}
  .cover-band .url{position:absolute;bottom:30px;left:0;right:0;text-align:center;color:var(--muted);font-size:11px}
  .swoosh{position:absolute;left:0;width:330px}

  /* outside left & middle */
  .dark{background:linear-gradient(180deg,var(--blue),var(--navy));color:var(--white)}
  .side-photo{position:absolute;top:0;left:0;width:330px;height:170px;background:linear-gradient(135deg,var(--photo-a),var(--photo-b))}
  .block{position:absolute;left:28px;right:28px}
  .head{font-family:"Montserrat",sans-serif;font-weight:800;font-size:18px;line-height:1.25}
  .head.orange{color:var(--orange)}
  .text{font-size:12px;line-height:1.55;color:var(--muted);margin-top:10px}
  .ticks{list-style:none;margin-top:16px}
  .ticks li{display:flex;align-items:center;gap:10px;font-size:13px;margin-bottom:10px;color:var(--white)}
  .ticks svg{flex:none}
  .button{display:inline-block;margin-top:18px;background:var(--orange);color:var(--white);font-family:"Montserrat",sans-serif;font-weight:600;font-size:12px;padding:8px 16px;border-radius:3px}
  .contact{font-size:12px;color:var(--white);display:flex;align-items:center;gap:8px;margin-top:10px}

  /* inside */
  .intro{background:var(--white)}
  .intro .brand{position:absolute;top:48px;left:28px}
  .intro .head{color:var(--blue)}
  .intro .text{color:var(--ink)}
  .intro-photo{position:absolute;bottom:0;left:0;width:330px;height:250px;background:radial-gradient(circle at 50% 60%,var(--photo-a),var(--photo-b))}
  .services{background:var(--navy)}
  .service{position:absolute;left:28px;right:28px;display:flex;gap:14px;align-items:flex-start}
  .service-icon{flex:none;width:54px;height:54px;border-radius:50%;background:var(--orange);display:flex;align-items:center;justify-content:center}
  .service h3{font-family:"Montserrat",sans-serif;font-weight:800;font-size:15px;color:var(--white);margin-top:6px}
  .service p{font-size:11.5px;color:var(--muted);line-height:1.45;margin-top:4px}
</style>
</head>
<body>

<!-- Front cover -->
<section class="panel cover solo">
  <div class="brand"><span class="brand-dot"></span>PELICAN FJORD</div>
  <h1 class="cover-title">IT SOLUTION DESIGNED FOR YOU</h1>
  <p class="cover-sub">Managed support that keeps your business running every day</p>
  <div class="cover-photo" role="img" aria-label="Photo of a hand touching glowing cloud and technology icons"></div>
  <svg class="swoosh" style="top:530px" width="330" height="40" viewBox="0 0 330 40"><path d="M0 30 Q165 -5 330 20 L330 40 L0 40Z" fill="#f28c1c"/><path d="M0 36 Q165 8 330 28 L330 40 L0 40Z" fill="#0d1f4d"/></svg>
  <div class="cover-band">
    <div class="cta">Call today for a free network review</div>
    <div class="url">pelicanfjordit.net</div>
  </div>
</section>

<!-- Outside spread -->
<div class="spread" style="top:820px">
  <section class="panel dark p1">
    <div class="side-photo" role="img" aria-label="Photo of a business person at a laptop"></div>
    <svg class="swoosh" style="top:150px" width="330" height="40" viewBox="0 0 330 40"><path d="M0 10 Q165 40 330 6 L330 40 L0 40Z" fill="#f28c1c"/><path d="M0 18 Q165 46 330 14 L330 40 L0 40Z" fill="#163a86"/></svg>
    <div class="block" style="top:220px">
      <h2 class="head orange">WHY CHOOSE US?</h2>
      <p class="text">Fast local support, clear pricing and proactive care for every device.</p>
      <ul class="ticks">
        <li><svg width="16" height="16" viewBox="0 0 16 16"><circle cx="8" cy="8" r="8" fill="#f28c1c"/><path d="M4 8.5l2.5 2.5L12 5.5" stroke="#fff" stroke-width="2" fill="none"/></svg>24/7 monitoring</li>
        <li><svg width="16" height="16" viewBox="0 0 16 16"><circle cx="8" cy="8" r="8" fill="#f28c1c"/><path d="M4 8.5l2.5 2.5L12 5.5" stroke="#fff" stroke-width="2" fill="none"/></svg>Cloud backup</li>
        <li><svg width="16" height="16" viewBox="0 0 16 16"><circle cx="8" cy="8" r="8" fill="#f28c1c"/><path d="M4 8.5l2.5 2.5L12 5.5" stroke="#fff" stroke-width="2" fill="none"/></svg>Help desk</li>
        <li><svg width="16" height="16" viewBox="0 0 16 16"><circle cx="8" cy="8" r="8" fill="#f28c1c"/><path d="M4 8.5l2.5 2.5L12 5.5" stroke="#fff" stroke-width="2" fill="none"/></svg>Security updates</li>
      </ul>
      <span class="button">pelicanfjordit.net</span>
    </div>
    <svg class="swoosh" style="bottom:0" width="330" height="60" viewBox="0 0 330 60"><path d="M0 50 Q165 0 330 30" stroke="#f28c1c" stroke-width="5" fill="none"/></svg>
  </section>

  <section class="panel dark p2">
    <div class="block" style="top:70px">
      <h2 class="head orange">THINKING BIG? THINK SMART</h2>
      <p class="text">We plan, build and manage IT so your team can focus on growth.</p>
    </div>
    <div class="block" style="top:250px;height:220px;left:0;right:0;background:linear-gradient(135deg,var(--photo-a),var(--photo-b))" role="img" aria-label="Photo of an office team working with computers"></div>
    <div class="block" style="top:520px">
      <div class="contact"><svg width="16" height="16" viewBox="0 0 16 16"><path d="M3 1h3l1 4-2 1a9 9 0 0 0 5 5l1-2 4 1v3a2 2 0 0 1-2 2A13 13 0 0 1 1 3a2 2 0 0 1 2-2z" fill="#f28c1c"/></svg>Phone: 555-0142</div>
      <div class="contact"><svg width="16" height="16" viewBox="0 0 16 16"><rect x="1" y="3" width="14" height="10" rx="1" fill="#f28c1c"/><path d="M1 4l7 5 7-5" stroke="#0d1f4d" stroke-width="1.5" fill="none"/></svg>info@pelicanfjordit.net</div>
    </div>
    <svg class="swoosh" style="bottom:0" width="330" height="60" viewBox="0 0 330 60"><path d="M0 30 Q165 60 330 20" stroke="#f28c1c" stroke-width="5" fill="none"/></svg>
  </section>

  <section class="panel cover p3">
    <div class="brand"><span class="brand-dot"></span>PELICAN FJORD</div>
    <h1 class="cover-title">IT SOLUTION DESIGNED FOR YOU</h1>
    <p class="cover-sub">Managed support that keeps your business running every day</p>
    <div class="cover-photo" role="img" aria-label="Photo of a hand touching glowing cloud and technology icons"></div>
    <svg class="swoosh" style="top:530px" width="330" height="40" viewBox="0 0 330 40"><path d="M0 30 Q165 -5 330 20 L330 40 L0 40Z" fill="#f28c1c"/><path d="M0 36 Q165 8 330 28 L330 40 L0 40Z" fill="#0d1f4d"/></svg>
    <div class="cover-band">
      <div class="cta">Call today for a free network review</div>
      <div class="url">pelicanfjordit.net</div>
    </div>
  </section>
</div>

<!-- Inside spread -->
<div class="spread" style="top:1620px">
  <section class="panel intro p1">
    <div class="brand"><span class="brand-dot"></span>PELICAN FJORD</div>
    <div class="block" style="top:130px">
      <h2 class="head">PELICAN FJORD IT SERVICES</h2>
      <p class="text">We are a managed services team helping local firms stay secure, connected and productive.</p>
    </div>
    <div class="intro-photo" role="img" aria-label="Photo of open hands holding a network of people icons"></div>
  </section>

  <section class="panel services p2">
    <div class="service" style="top:70px"><div class="service-icon"><svg width="26" height="26" viewBox="0 0 26 26"><rect x="3" y="5" width="20" height="13" rx="1" fill="none" stroke="#fff" stroke-width="2"/><path d="M9 22h8M13 18v4" stroke="#fff" stroke-width="2"/></svg></div><div><h3>Network Care</h3><p>Short text about this service for your team.</p></div></div>
    <div class="service" style="top:290px"><div class="service-icon"><svg width="26" height="26" viewBox="0 0 26 26"><path d="M7 19a5 5 0 0 1 0-10 7 7 0 0 1 13 2 4 4 0 0 1 0 8z" fill="#fff"/></svg></div><div><h3>Cloud Services</h3><p>Short text about this service for your team.</p></div></div>
    <div class="service" style="top:510px"><div class="service-icon"><svg width="26" height="26" viewBox="0 0 26 26"><ellipse cx="13" cy="6" rx="8" ry="3" fill="#fff"/><path d="M5 6v14c0 2 16 2 16 0V6" fill="none" stroke="#fff" stroke-width="2"/></svg></div><div><h3>Data Backup</h3><p>Short text about this service for your team.</p></div></div>
  </section>

  <section class="panel services p3">
    <div class="service" style="top:70px"><div class="service-icon"><svg width="26" height="26" viewBox="0 0 26 26"><path d="M13 2l9 4v7c0 6-4 9-9 11-5-2-9-5-9-11V6z" fill="#fff"/></svg></div><div><h3>Cyber Security</h3><p>Short text about this service for your team.</p></div></div>
    <div class="service" style="top:290px"><div class="service-icon"><svg width="26" height="26" viewBox="0 0 26 26"><path d="M5 15v-3a8 8 0 0 1 16 0v3" fill="none" stroke="#fff" stroke-width="2"/><rect x="3" y="14" width="5" height="7" rx="1" fill="#fff"/><rect x="18" y="14" width="5" height="7" rx="1" fill="#fff"/></svg></div><div><h3>Help Desk</h3><p>Short text about this service for your team.</p></div></div>
    <div class="service" style="top:510px"><div class="service-icon"><svg width="26" height="26" viewBox="0 0 26 26"><path d="M4 20l6-6 4 4 8-9" fill="none" stroke="#fff" stroke-width="2.5"/><path d="M17 9h5v5" fill="none" stroke="#fff" stroke-width="2.5"/></svg></div><div><h3>Consulting</h3><p>Short text about this service for your team.</p></div></div>
  </section>
</div>

</body>
</html>
```